Sign Advertisment for Condominium Development

I need a sign created that will be placed in front of a building that is being converted into a luxury condominium development.

The sign needs to say:

Two, Boutique Luxury Condominiums Delivering late 2015.

Luxury Finishes // Designer Kitchens and Bath // Each Unit over 2,000 Square Feet

Deeded Parking Included with Each Unit

To Learn More, Contact:

Marissa Talbot or Vernon Pike
(202) 555-0147
Marissa.Talbot@example-realty.com

I need a small disclaimer at the bottom stating:

These Condominium(s) have not been registered by the Office of Residential Standards and Property Oversight Bureau Tenancy Transition and Transfer Section. A Condominium Unit may be reserved on a non-binding reservation agreement, but no contract of sale or lease that is binding on the purchaser may be entered into prior to registration.

Target Market(s)

Young professionals seeking luxury condominium

Industry/Entity Type

Building

Font styles to use
Serif

Colors
00a88f
ffffff

```html
<!DOCTYPE html>
<html lang="en">
<head>
<meta charset="utf-8">
<title>Boutique Luxury Condominiums — Sign</title>
<link href="https://fonts.googleapis.com/css2?family=Crimson+Pro:ital,wght@0,400;1,400&family=Tinos:ital@0;1&display=swap" rel="stylesheet">
<style>
  :root {
    --brand-green: #17a98e;
    --ink-white: #ffffff;
    --rule-white: rgba(255, 255, 255, 0.8);
  }
  html, body {
    margin: 0;
    padding: 0;
    overflow: hidden;
    background: var(--brand-green);
  }
  .sign {
    position: relative;
    width: 1200px;
    height: 800px;
    background: var(--brand-green);
    color: var(--ink-white);
    font-family: "Tinos", "Times New Roman", serif;
    overflow: hidden;
  }
  .line {
    position: absolute;
    left: 0;
    right: 0;
    margin: 0;
    text-align: center;
    white-space: nowrap;
    font-weight: 400;
  }
  .eyebrow {
    top: 84px;
    font-family: "Crimson Pro", "Times New Roman", serif;
    font-size: 73px;
    line-height: 73px;
    letter-spacing: 1px;
  }
  .eyebrow .dot { margin: 0 6px; position: relative; top: -6px; font-size: 40px; }
  .headline {
    top: 160px;
    font-family: "Crimson Pro", "Times New Roman", serif;
    font-style: italic;
    font-size: 158px;
    line-height: 158px;
    letter-spacing: 2px;
  }
  .delivery {
    top: 318px;
    font-family: "Crimson Pro", "Times New Roman", serif;
    font-size: 52px;
    line-height: 52px;
    letter-spacing: 1px;
  }
  .delivery-rules {
    position: absolute;
    left: 0;
    top: 0;
  }
  .features {
    font-size: 20px;
    line-height: 20px;
    letter-spacing: 0.4px;
  }
  .features--one { top: 410px; }
  .features--two { top: 445px; }
  .divider {
    display: inline-block;
    width: 0;
    height: 22px;
    border-left: 1px solid var(--rule-white);
    margin: 0 16px;
    vertical-align: -4px;
  }
  .contact-lead {
    top: 538px;
    font-size: 18px;
    line-height: 18px;
    letter-spacing: 0.4px;
  }
  .contact-names {
    top: 570px;
    font-size: 28px;
    line-height: 28px;
    letter-spacing: 0.6px;
  }
  .contact-names em { text-transform: none; letter-spacing: 0; }
  .contact-details {
    top: 612px;
    font-size: 28px;
    line-height: 30px;
  }
  .contact-details em { font-style: italic; }
  .contact-details .divider { height: 26px; margin: 0 20px; vertical-align: -4px; }
  .disclaimer {
    top: 717px;
    font-size: 13px;
    line-height: 22px;
    white-space: normal;
    padding: 0 40px;
  }
</style>
</head>
<body>
<main class="sign">
  <p class="line eyebrow">TWO<span class="dot">·</span>BOUTIQUE<span class="dot">·</span>LUXURY</p>
  <h1 class="line headline">Condominiums</h1>

  <svg class="delivery-rules" width="1200" height="800" aria-hidden="true">
    <g stroke="#ffffff" stroke-width="1" fill="#ffffff">
      <circle cx="136" cy="341" r="3" stroke="none"/>
      <line x1="136" y1="341" x2="280" y2="341"/>
      <line x1="287.5" y1="320" x2="287.5" y2="362"/>
      <line x1="912.5" y1="320" x2="912.5" y2="362"/>
      <line x1="920" y1="341" x2="1064" y2="341"/>
      <circle cx="1064" cy="341" r="3" stroke="none"/>
    </g>
  </svg>
  <h2 class="line delivery">DELIVERING LATE 2015</h2>

  <p class="line features features--one">LUXURY FINISHES<span class="divider"></span>DESIGNER KITCHENS AND BATH</p>
  <p class="line features features--two">EACH UNIT OVER 2,000 SQUARE FEET<span class="divider"></span>DEEDED PARKING INCLUDED WITH EACH UNIT</p>

  <p class="line contact-lead">TO LEARN MORE, CONTACT:</p>
  <p class="line contact-names">MARISSA TALBOT <em>or</em> VERNON PIKE</p>
  <p class="line contact-details">(202) 555-0147<span class="divider"></span><em>Marissa.Talbot@example-realty.com</em></p>

  <p class="line disclaimer">These Condominium(s) have not been registered by the Office of Residential Standards and Property Oversight Bureau Tenancy Transition and Transfer Section.<br>A Condominium Unit may be reserved on a non-binding reservation agreement, but no contract of sale or lease that is binding on the purchaser may be entered into prior to registration.</p>
</main>
</body>
</html>
```